Joli Matin Re Design

as per discussion on message board Kemberly!

remove the following from the back of the card:
address and replace with Brisbane and Perth and please remove the land line phone number 07 4829 1530.

please ensure that the back of the card looks balanced with this all being removed.

thank you!

```html
<!DOCTYPE html>
<html lang="en">
<head>
<meta charset="utf-8">
<title>Joli Matin – Business Card</title>
<link rel="stylesheet" href="https://fonts.googleapis.com/css2?family=Questrial&family=Didact+Gothic&display=swap">
<style>
  :root {
    --backdrop: #2e2e2e;
    --card-white: #ffffff;
    --card-grey: #9c9c9c;
    --card-grey-dark: #8a8a8a;
    --ink-strong: #8c8c8c;
    --ink-soft: #a6a6a6;
    --ink-dark: #555555;
    --frame-line: #e6e6e6;
    --ornament-light: #b4b4b4;
    --ornament-pale: #f1f1f1;
  }
  * { margin: 0; padding: 0; box-sizing: border-box; }
  html, body {
    width: 1200px; height: 800px; overflow: hidden;
    background: var(--backdrop);
    font-family: "Questrial", "Didact Gothic", sans-serif;
  }
  .stage {
    width: 1200px; height: 800px;
    display: flex; align-items: center; justify-content: center; gap: 60px;
  }
  .card {
    position: relative;
    width: 525px; height: 300px;
    border-radius: 22px;
    overflow: hidden;
  }

  /* Back of card */
  .card--back { background: var(--card-white); }
  .contact {
    position: absolute; left: 34px; top: 30px;
    color: var(--ink-soft); font-size: 13px; line-height: 1.45;
  }
  .contact__name { color: var(--ink-strong); font-size: 20px; font-weight: 700; letter-spacing: 0.2px; }
  .contact__title { font-size: 14px; margin-bottom: 6px; }
  .contact__label { color: var(--ink-strong); font-weight: 700; }
  .contact__strong { color: var(--ink-strong); font-weight: 700; }
  .tagline {
    position: absolute; left: 26px; bottom: 26px;
    font-family: "Didact Gothic", sans-serif;
    font-size: 33px; color: var(--ink-dark); letter-spacing: 0.3px;
  }
  .tagline .dot { font-size: 26px; color: var(--ink-dark); }
  .brand-mini {
    position: absolute; right: 30px; top: 34px;
    width: 170px; height: 120px;
  }
  .brand-mini__ornament {
    position: absolute; inset: 0; border-radius: 50%;
    background: radial-gradient(ellipse at center, var(--card-white) 55%, var(--ornament-pale) 80%, #e2e2e2 100%);
  }
  .brand-mini__name {
    position: absolute; inset: 0;
    display: flex; align-items: center; justify-content: center;
    font-size: 20px; color: var(--ink-dark);
  }
  .location {
    position: absolute; right: 38px; top: 172px;
    text-align: right; color: var(--ink-soft); font-size: 15px; line-height: 1.5;
  }

  /* Front of card */
  .card--front { background: linear-gradient(160deg, var(--card-grey) 0%, var(--card-grey-dark) 100%); }
  .card__border {
    position: absolute; inset: 12px;
    border: 1.5px solid var(--frame-line); border-radius: 16px;
  }
  .brand {
    position: absolute; left: 50%; top: 50%;
    width: 270px; height: 190px; transform: translate(-50%, -50%);
  }
  .brand__ornament {
    position: absolute; inset: 0; border-radius: 50%;
    background: radial-gradient(ellipse at center, var(--card-grey) 55%, var(--ornament-light) 82%, var(--card-grey) 100%);
  }
  .brand__name {
    position: absolute; inset: 0;
    display: flex; align-items: center; justify-content: center;
    font-size: 34px; color: var(--card-white);
  }
</style>
</head>
<body>
<main class="stage">
  <section class="card card--back" aria-label="Card back">
    <div class="contact">
      <p class="contact__name">Mara Delvecchio</p>
      <p class="contact__title">Director / Events Manager / Stylist</p>
      <p><span class="contact__label">email:</span> mara@<span class="contact__strong">jolimatinevents</span>.com.au</p>
      <p><span class="contact__label">web:</span> www.<span class="contact__strong">jolimatinevents</span>.com.au</p>
    </div>
    <div class="brand-mini">
      <div class="brand-mini__ornament" role="img" aria-label="Ornamental scroll frame around the brand name"></div>
      <p class="brand-mini__name">Joli Matin</p>
    </div>
    <div class="location">
      <p><span class="contact__label">cell:</span> 0412 580 273</p>
      <p>Perth and Brisbane</p>
    </div>
    <p class="tagline"><span class="dot">•</span>design <span class="dot">•</span>create <span class="dot">•</span>celebrate<span class="dot">•</span></p>
  </section>

  <section class="card card--front" aria-label="Card front">
    <div class="card__border"></div>
    <div class="brand">
      <div class="brand__ornament" role="img" aria-label="Embossed ornamental scroll frame around the brand name"></div>
      <p class="brand__name">Joli Matin</p>
    </div>
  </section>
</main>
</body>
</html>
```